Full-Size Brochure for Medical Mobile App (Zorvek)

I am looking for a full-size brochure for a mobile app (Zorvek - not on Maltoby) that is used in the pharmaceutical clinical trial industry of 8 pages (Letter format). The total content is about 1000 words (attached). This brochure needs to be an attractive design and the design should support the content. The goal of the brochure to persuade people to try the application, so it needs to be inviting to read and save the brochure. We need to print this as well as be able to distribute this as a PDF, so we need a small size PDF file and a high res print-ready PDF. The brochure needs to be designed in accordance with the brandbook (attached). A mockup (for screenshots) of the application can be found at: https://proto.quenvia-example.net/view/3c9a1e2d-58b4-4f0e-a7d1-9e2b6f4c8a10/

Target Market(s)

Pharmaceutical companies. CRO's and Central Laboratories

Industry/Entity Type

Medical And Science

Other font styles liked:
• See brandbook

Requirements
Must have
• Must have a sleek design that invites to read the content.
Nice to have
• Some added (generic) graphics to support the content.

```html
<!DOCTYPE html>
<html lang="en">
<head>
<meta charset="utf-8">
<title>Specora Brochure – Spread</title>
<link rel="stylesheet" href="https://fonts.googleapis.com/css2?family=Montserrat:wght@400;500&family=Arimo:wght@400&family=Roboto+Condensed:wght@400;500&display=swap">
<style>
  :root {
    --brand-blue: #1d4fb3;
    --brand-blue-deep: #1a46a3;
    --ink-blue: #2450b5;
    --paper: #ffffff;
    --backdrop: #e9eaec;
    --band-text: #ffffff;
  }
  html, body { margin: 0; padding: 0; overflow: hidden; }
  body {
    width: 1200px; height: 1200px;
    background: var(--backdrop);
    display: flex; align-items: center; justify-content: center;
  }
  .spread { display: flex; width: 1100px; height: 712px; box-shadow: 0 4px 18px rgba(0,0,0,.12); }
  .page { width: 550px; height: 712px; background: var(--paper); position: relative; overflow: hidden; }

  /* Left page */
  .page--left .frame {
    position: absolute; inset: 12px 12px 12px 14px;
    border: 2px solid var(--brand-blue);
  }
  .intro, .lead {
    position: absolute; left: 28px; right: 26px;
    font-family: "Montserrat", sans-serif; color: var(--ink-blue);
    font-size: 9.2px; line-height: 15.5px; text-align: justify; text-align-last: center;
    margin: 0;
  }
  .intro { top: 30px; }
  .lead { top: 120px; }
  .feature-image {
    position: absolute; left: 30px; right: 28px; top: 236px; height: 168px;
    background: linear-gradient(120deg, #eaf3fb 0%, #bfe0f5 35%, #5fb4e6 65%, #1e6fc0 100%);
  }
  .problems {
    position: absolute; left: 14px; right: 12px; top: 424px; bottom: 12px;
    background: var(--brand-blue-deep); color: var(--band-text);
  }
  .problems .inner-frame {
    position: absolute; inset: 6px 8px 8px 8px; border: 1.5px solid rgba(255,255,255,.85);
    padding: 12px 14px 0 18px;
  }
  .problems h2 {
    font-family: "Montserrat", sans-serif; font-weight: 400; font-size: 16px;
    margin: 0 0 6px 0; letter-spacing: .2px;
  }
  .problems ul { margin: 0; padding-left: 10px; list-style: none; }
  .problems li {
    font-family: "Arimo", sans-serif; font-size: 8.4px; line-height: 11.6px;
    position: relative; margin-bottom: 2px;
  }
  .problems li::before { content: "•"; position: absolute; left: -9px; }

  /* Right page */
  .page--right { display: flex; }
  .side-column { width: 172px; padding: 26px 12px 0 14px; box-sizing: border-box; color: var(--ink-blue); font-family: "Roboto Condensed", sans-serif; }
  .side-column h2 { font-size: 14.5px; font-weight: 500; line-height: 20px; margin: 0 0 10px 0; }
  .divider { width: 118px; height: 3px; background: var(--brand-blue); margin-bottom: 14px; }
  .citation { font-size: 8.2px; line-height: 14.2px; margin: 0 0 20px 0; }
  .side-column h3 { font-size: 13.5px; font-weight: 500; margin: 0 0 14px 0; }
  .body-copy { font-size: 8.2px; line-height: 15px; text-align: justify; margin: 0 0 16px 0; }
  .hero-photo {
    flex: 1;
    background:
      radial-gradient(circle at 30% 25%, #dff3ff 0%, rgba(120,200,240,.7) 18%, transparent 38%),
      radial-gradient(circle at 78% 12%, #ff5fb2 0%, rgba(214,60,160,.7) 20%, transparent 40%),
      radial-gradient(circle at 75% 50%, #ff8a3a 0%, rgba(230,90,40,.8) 18%, transparent 36%),
      radial-gradient(circle at 25% 70%, #18c9c0 0%, rgba(30,150,170,.7) 20%, transparent 42%),
      radial-gradient(circle at 80% 85%, #ff7a40 0%, transparent 30%),
      linear-gradient(160deg, #2a6fd0 0%, #2b1860 55%, #080812 100%);
  }
</style>
</head>
<body>
  <div class="spread">
    <section class="page page--left">
      <div class="frame"></div>
      <p class="intro">In the world of clinical trials, the loss of specimens can be catastrophic. Not only the financial implications, but especially the scientific value of a unique specimen can make them priceless. And yet, many clinical trials still rely on specimen collection containers that are labeled at the site using blank labels and sharpies.</p>
      <p class="lead">Handwritten specimen labels have the highest failure rates when it comes to sample loss. But the problem doesn’t stop with just the labels. When the samples are shipped to the laboratory for analysis, a handwritten requisition form generally accompanies them. So, even though Clinical Trial Management Software (CTMS) is implemented in order to manage, track and report on collected sample data, there is still a blind spot from the moment the sample is collected, until it is entered into the Laboratory Information Management System (LIMS).</p>
      <div class="feature-image" role="img" aria-label="Laboratory flasks with blue liquid in front of a printed bar chart"></div>
      <div class="problems">
        <div class="inner-frame">
          <h2>Identified Problems in The Industry Today:</h2>
          <ul>
            <li>Over half of all identification errors in the lab result from bad specimen labels (i.e., illegible handwriting, spelling errors, inconsistent date notation, wrong subject ID, etc.)</li>
            <li>Few or no barcodes on specimen labels. Barcodes allow for subject/specimen information to be transmitted and stored electronically, reducing the need for human manual data entry, and centralizing the information in a secure database</li>
            <li>Insufficient number of barcodes complicates the process of correlating information to provide a clear chain-of-custody record, which in turn complicates attempts to identify and correct errors that may already exist but have gone undetected</li>
            <li>Clinical trial sites must allocate valuable site space to accommodate influx of study-specific collection kits and materials. This is not a smart or efficient use of lab space.</li>
            <li>Following or amending protocol is time-consuming, slow, and expensive (i.e., in the event of a change of protocol, current kits must be discarded, and new kits must be sourced, packed, and shipped to the site, old protocol binders must be discarded, and new protocol binders must be printed and shipped to the site, etc.)</li>
            <li>Project managers cannot get real-time, up-to-date insight into the progress of all sites participating in the study. The transfer of information is delayed.</li>
            <li>Laboratories miss the opportunity to conserve valuable time because they are not provided with accurate forecasts regarding when certain samples will be arriving at their facility</li>
          </ul>
        </div>
      </div>
    </section>

    <section class="page page--right">
      <div class="side-column">
        <h2>Specora was designed to fill the information gap between the time of sample collection and arrival at the lab.</h2>
        <div class="divider"></div>
        <p class="citation">Lena R. Vostrik, Omar Delacroix, Priya Thandeka, Jonas Wellbury, Mei-Lin Okafor, Tomas Reinholt, Ada K. Sorensen. Significant Reduction of Laboratory Specimen Labeling Errors by Implementation of an Electronic Ordering System Paired With a Bar-Code Specimen Labeling Process. Journal of Acute Care Practice 2010;56(6):630-636</p>
        <h3>How does it work?</h3>
        <p class="body-copy">During the visit, the application will guide the user through which samples need to be collected and how they will need to be processed, stored, and shipped. All specimen labels are printed instantly. When samples are ready to be shipped, the application allows the user to select the samples contained in the shipment and print a requisition form, containing all sample related information.</p>
        <p class="body-copy">Upon completion of the visit, the investigator can indicate whether the specimens will be stored at the site for a consolidated shipment to the lab or if they will be shipped right away. The application will capture the shipment tracking details and printing the requisition form that will go with the shipment. This information will be posted to the database, which allows the Project Manager to gain real-time insight into collection progress and sample locations.</p>
      </div>
      <div class="hero-photo" role="img" aria-label="Close-up of glass laboratory flasks glowing in blue, pink, orange and teal light"></div>
    </section>
  </div>
</body>
</html>
```